IT support company needs Banner Ad for the top of their quote layout template

We need a banner Ad for the top of our for quote layout template so it is sent out on all our quotes

The banner size must be 827 x 100 pixels - anything larger than 60 KB can cause upload time issues

We have attached our logo and examples of the quote page to see how it looks in the context of the whole page.

Essential elements of the banner
- Must have our logo but this can be changed to be different colours if it makes the design work better i.e. Tidal Grove could be all in white

Colours
- Can use all of our standard colours - Orange, Black, Grey and White

Images
- As a premium IT support company we deal with people and technology so would like to see both of these Incorporated into the banner i.e. people using technology These images could be watermarked or one colour effect.

Look and Feel
- Professional, friendly, people, technology, premium

Target Market
Small business owners and managers

Industry/Entity Type

It Company

```html
<!DOCTYPE html>
<html lang="nl">
<head>
<meta charset="utf-8">
<title>Standard MSP #2 – Offerte</title>
<link rel="stylesheet" href="https://fonts.googleapis.com/css2?family=Carlito:wght@400;700&display=swap">
<style>
:root{
  --ink:#111111;
  --brand-blue:#1f6fc4;
  --rule-blue:#1a6fc9;
  --label-blue:#2e74b5;
  --head-light:#d3e8f8;
  --head-mid:#b8dbf4;
  --row-alt:#f2f2f2;
  --banner-left-a:#c9dcec;
  --banner-left-b:#eaf2f9;
  --banner-photo-a:#6f7f92;
  --banner-photo-b:#dfe6ee;
  --logo-orange:#f26a1b;
  --portrait:#5a5a5a;
  --white:#ffffff;
}
*{box-sizing:border-box;margin:0;padding:0}
html,body{width:1200px;height:1002px;overflow:hidden;background:var(--white)}
body{font-family:"Carlito",sans-serif;color:var(--ink);position:relative}
.abs{position:absolute}

.banner{left:0;top:0;width:1200px;height:150px;display:flex}
.banner-art{flex:0 0 760px;background:linear-gradient(90deg,var(--banner-left-a),var(--banner-left-b))}
.banner-photo{flex:1;background:linear-gradient(90deg,var(--banner-left-b),var(--banner-photo-b) 15%,var(--banner-photo-a))}
.banner-logo{left:285px;top:42px;width:452px;font-size:64px;font-weight:700;color:var(--logo-orange);letter-spacing:6px;line-height:64px;white-space:nowrap}
.banner-rule{left:0;top:150px;width:1200px;height:6px;background:var(--brand-blue)}

.doc-title{left:40px;top:209px;font-size:27px;line-height:30px;font-weight:400}
.portrait{left:39px;top:262px;width:142px;height:189px;background:linear-gradient(160deg,#8a8a8a,var(--portrait))}

.party{top:262px;font-size:18.5px;line-height:24px}
.party h2{font-size:22px;font-weight:400;color:var(--label-blue);line-height:28px;margin-bottom:6px}
.party p{height:24.5px;white-space:nowrap}
.party .strong{font-weight:700}
.party .gap{height:24px}
.from{left:197px}
.to{left:522px}
.meta{left:907px}
.meta p{height:27px}

.section-rule{left:39px;top:467px;width:1122px;height:4px;background:var(--rule-blue)}
.section-title{left:40px;font-size:24px;line-height:28px;font-weight:400}

.items{left:39px;width:1122px;border-collapse:collapse;font-size:18.5px;border-left:1.5px solid var(--ink);border-right:1.5px solid var(--ink);border-bottom:1.5px solid var(--ink)}
.items th,.items td{padding:0 8px;height:37px;text-align:left;font-weight:400}
.items thead tr{background:linear-gradient(90deg,var(--head-mid),var(--head-light) 50%,var(--head-mid))}
.items thead{border-top:1.5px solid var(--ink);border-bottom:1.5px solid var(--ink)}
.items .amount{text-align:right;width:159px;border-left:1.5px solid var(--ink)}
.items tbody tr:nth-child(even){background:var(--row-alt)}

.totals{right:49px;font-size:18.5px;line-height:36.5px}
.totals .row{display:flex;justify-content:flex-end}
.totals .label{color:var(--label-blue);text-align:right}
.totals .value{font-weight:700;width:156px;text-align:right}
</style>
</head>
<body>
<header>
  <div class="abs banner">
    <div class="banner-art" role="img" aria-label="Blauwe illustratie van een netwerk van verbonden personen-iconen"></div>
    <div class="banner-photo" role="img" aria-label="Foto van collega's die samen aan laptops werken in een kantoor"></div>
  </div>
  <div class="abs banner-logo">TIDAL GROVE</div>
  <div class="abs banner-rule"></div>
</header>

<h1 class="abs doc-title">Standard MSP&nbsp;&nbsp;#2</h1>

<div class="abs portrait" role="img" aria-label="Portretfoto van de opsteller van de offerte"></div>

<section class="abs party from">
  <h2>Opgesteld door:</h2>
  <p class="strong">Marten Hale Inc</p>
  <p>Marten Hale</p>
  <p class="gap"></p>
  <p>Fax</p>
  <p>marten.hale@quotewell.com</p>
</section>

<section class="abs party to">
  <h2>Opgesteld voor:</h2>
  <p class="strong">Copper Ridge</p>
  <p>2718 Linden Rd.</p>
  <p>Ashford,&nbsp;&nbsp;40382</p>
  <p>Rosalind Park</p>
  <p>rosa.park@bluefinch.co.uk</p>
</section>

<section class="abs party meta">
  <h2>Gegevens Offerte:</h2>
  <p class="strong">Offerte #: MH-000280</p>
  <p>Versie: 1</p>
  <p>Leverdatum: 14/11/2017</p>
  <p>Vervaldatum: 31/12/2017</p>
</section>

<div class="abs section-rule"></div>

<h2 class="abs section-title" style="top:498px">Overzicht Offerte</h2>
<table class="abs items" style="top:537px">
  <thead><tr><th>Beschrijving</th><th class="amount">Bedrag</th></tr></thead>
  <tbody><tr><td>Initial Investment</td><td class="amount">$800.00</td></tr></tbody>
</table>

<div class="abs totals" style="top:615px">
  <div class="row"><span class="label">Subtotaal:</span><span class="value">$800.00</span></div>
  <div class="row"><span class="label">VAT:</span><span class="value">$160.00</span></div>
  <div class="row"><span class="label">Totaal:</span><span class="value">$960.00</span></div>
</div>

<h2 class="abs section-title" style="top:753px">Overzicht Terugkerende Kosten</h2>
<table class="abs items" style="top:792px">
  <thead><tr><th>Beschrijving</th><th class="amount">Bedrag</th></tr></thead>
  <tbody>
    <tr><td>Monitoring</td><td class="amount">$375.00</td></tr>
    <tr><td>Support</td><td class="amount">$65.00</td></tr>
    <tr><td>Fixed Hours</td><td class="amount">$850.00</td></tr>
  </tbody>
</table>

<div class="abs totals" style="top:946px">
  <div class="row"><span class="label">Terugkerende totaal:</span><span class="value">$1,290.00</span></div>
</div>
</body>
</html>
```